Our Family Values Printed on Canvas for our Home

My family has decided on the following values:

Be Grateful
Act Kindly
Stay Honest
Smile Often
Do Your Best
Live Adventurously
Never Stop Learning
Help Others
Love Always

We desire to print a sign (on 16x20 or 20x16 canvas) for various rooms in our house to remind us of the family we want to be. Each value has equal value, and we want the sign to reflect that (for example, we don't want one value to appear larger than another). We are not particular about colors or images however here are some hints about us that may help:
- My wife's favorite color is dark teal
- We live in the Pacific Northwest
- We love nature
- My wife and I have two sons and a dog

We look forward to your design!

--Corwin

Target Market(s)

Our family and friends

Industry/Entity Type

Non-Profit

Font styles to use
Decorative

Requirements
Must have
• - Printable on 16x20 or 20x60 canvas
• - Equal emphasis on each value
• - Easy to read

```html
<!DOCTYPE html>
<html lang="en">
<head>
<meta charset="utf-8">
<title>Family Values Canvas Sign</title>
<link rel="stylesheet" href="https://fonts.googleapis.com/css2?family=Montserrat:wght@300;700&display=swap">
<style>
  :root {
    --page-bg: #ffffff;
    --teal-deep: #07202b;
    --teal-dark: #0d3444;
    --teal-mid: #155069;
    --teal-glow: #2a7f9c;
    --text-light: #ffffff;
  }
  html, body {
    margin: 0;
    padding: 0;
    width: 1200px;
    height: 1200px;
    overflow: hidden;
    background: var(--page-bg);
  }
  .canvas {
    position: relative;
    width: 1200px;
    height: 1200px;
    display: flex;
    align-items: center;
    justify-content: center;
  }
  .sign {
    position: relative;
    width: 1100px;
    height: 866px;
    overflow: hidden;
  }
  .sign__backdrop {
    position: absolute;
    inset: 0;
    background:
      radial-gradient(ellipse 45% 40% at 58% 55%, rgba(42,127,156,0.55), transparent 70%),
      radial-gradient(ellipse 30% 35% at 88% 40%, rgba(42,127,156,0.45), transparent 70%),
      radial-gradient(ellipse 35% 30% at 20% 80%, rgba(21,80,105,0.6), transparent 70%),
      radial-gradient(ellipse 40% 35% at 15% 20%, rgba(7,32,43,0.9), transparent 70%),
      linear-gradient(135deg, var(--teal-deep) 0%, var(--teal-dark) 40%, var(--teal-mid) 70%, var(--teal-dark) 100%);
  }
  .values {
    position: absolute;
    inset: 0;
    margin: 0;
    padding: 0;
    list-style: none;
    display: flex;
    flex-direction: column;
    align-items: center;
    justify-content: center;
    color: var(--text-light);
    font-family: "Montserrat", sans-serif;
    font-size: 61px;
    line-height: 87px;
    text-align: center;
  }
  .values__item--light {
    font-weight: 300;
    letter-spacing: 1px;
  }
  .values__item--bold {
    font-weight: 700;
    letter-spacing: -0.5px;
  }
</style>
</head>
<body>
  <main class="canvas">
    <section class="sign">
      <div class="sign__backdrop" role="img" aria-label="Close-up photograph of soft dark teal feathers"></div>
      <ul class="values">
        <li class="values__item--light">Be Grateful</li>
        <li class="values__item--bold">Act Kindly</li>
        <li class="values__item--light">Stay Honest</li>
        <li class="values__item--bold">Smile Often</li>
        <li class="values__item--light">Do Your Best</li>
        <li class="values__item--bold">Live Adventurously</li>
        <li class="values__item--light">Never Stop Learning</li>
        <li class="values__item--bold">Help Others</li>
        <li class="values__item--light">Love Always</li>
      </ul>
    </section>
  </main>
</body>
</html>
```